Wren's Hearth Support Business Card

Business card design
Font must be in Poppins Regular for Wren's Hearth Support
Safe Days Ahead font is Alex Brush

Colour must be Hex #910E2B
RGB 145-14-43
Pantone 7427 C
We want the card editable
On the front please include
Name eg Mavis Dunleavy
Position eg Clinical Care Manager
Phone number mobile 0473 856 342
Phone 08 7394 2650
Email : mavis@wrenshearthsupport.com.au
Address : Gullwing Cove, Western Australia, 6291
Website : wrenshearthsupport.com.au
Contact us today to experience the warmth, respect and personal touch of Wren's Hearth Support.

Target Market(s)

35+

Industry/Entity Type

aged care / community

Contact Information for Business Card

see project description

Requirements
Must have
• Colours, logos and fonts as detailed and uploaded

```html
<!DOCTYPE html>
<html lang="en">
<head>
<meta charset="utf-8">
<title>Wren's Hearth Support – Business Card</title>
<link href="https://fonts.googleapis.com/css2?family=Alex+Brush&family=Poppins:wght@400;700&display=swap" rel="stylesheet">
<style>
  :root {
    --brand: #910E2B;
    --blush: #E0C1C9;
    --stage: #CCCCCC;
    --card: #FFFFFF;
    --ink: #555555;
    --pattern-a: #FDF3F4;
    --pattern-b: #FFFFFF;
  }
  * { margin: 0; padding: 0; box-sizing: border-box; }
  html, body {
    width: 1200px; height: 1111px; overflow: hidden;
    background: var(--stage);
  }
  .canvas { position: relative; width: 1200px; height: 1111px; }
  .side-label {
    position: absolute;
    font-family: 'Poppins', sans-serif;
    font-weight: 700;
    font-size: 30px;
    line-height: 1;
    color: var(--brand);
  }
  .side-label--front { left: 74px; top: 43px; }
  .side-label--back { left: 371px; top: 561px; }

  .card {
    position: absolute;
    width: 754px; height: 442px;
    background: var(--card);
    overflow: hidden;
  }
  .card--front { left: 75px; top: 75px; }
  .card--back { left: 372px; top: 592px; }

  .card__pattern {
    position: absolute; inset: 0;
    background: radial-gradient(circle at 30% 40%, var(--pattern-a), var(--pattern-b) 60%),
                radial-gradient(circle at 75% 70%, var(--pattern-a), transparent 55%);
  }
  .card__corners { position: absolute; inset: 0; width: 754px; height: 442px; }
  .corner--brand { fill: var(--brand); }
  .corner--blush { fill: var(--blush); }

  /* Front brand lockup */
  .brand-ring {
    position: absolute;
    border: 5px solid var(--brand);
    border-radius: 50%;
  }
  .card--front .brand-ring { left: 190px; top: 150px; width: 120px; height: 120px; }
  .brand-name {
    position: absolute;
    left: 322px; top: 140px;
    font-family: 'Poppins', sans-serif;
    font-weight: 400;
    font-size: 42px;
    line-height: 46px;
    color: var(--brand);
    white-space: nowrap;
  }
  .tagline {
    position: absolute;
    left: 324px; top: 240px;
    font-family: 'Alex Brush', cursive;
    font-size: 32px;
    line-height: 1;
    color: var(--brand);
  }

  /* Back */
  .card--back .brand-ring { left: 119px; top: 37px; width: 90px; height: 90px; border-width: 4px; }
  .person {
    position: absolute; left: 244px; top: 48px;
    font-family: 'Poppins', sans-serif;
    color: var(--brand);
    white-space: nowrap;
  }
  .person__name { font-weight: 700; font-size: 38px; line-height: 42px; }
  .person__role { font-weight: 400; font-size: 22px; line-height: 26px; letter-spacing: 0.16em; }

  .contacts {
    position: absolute; left: 128px; top: 193px;
    list-style: none;
    font-family: 'Poppins', sans-serif;
    font-size: 21px;
    color: var(--ink);
  }
  .contacts__item {
    display: flex; align-items: center;
    height: 30px;
    white-space: nowrap;
  }
  .contacts__item:nth-child(2) { margin-top: 12px; }
  .contacts__item:nth-child(3) { margin-top: 8px; }
  .contacts__item:nth-child(4) { margin-top: 6px; }
  .contacts__item:nth-child(5) { margin-top: 12px; }
  .contacts__icon { width: 24px; height: 24px; margin-right: 14px; fill: var(--brand); flex: none; }
</style>
</head>
<body>
<div class="canvas">

  <div class="side-label side-label--front">FRONT</div>
  <section class="card card--front">
    <div class="card__pattern" role="img" aria-label="Faint pattern of pale red flowers with thin stems across the card"></div>
    <svg class="card__corners" viewBox="0 0 754 442" aria-hidden="true">
      <path class="corner--brand" d="M0 0H50C46 72 36 140 0 174Z"/>
      <path class="corner--blush" d="M626 0C626 62 670 102 740 102H754V20H706C692 20 684 12 684 0Z"/>
      <path class="corner--blush" d="M0 334C62 336 116 380 144 442H34C33 418 22 410 0 408Z"/>
      <path class="corner--brand" d="M647 442C647 372 690 330 754 315V442Z"/>
    </svg>
    <div class="brand-ring" aria-hidden="true"></div>
    <div class="brand-name">Wren's<br>Hearth Support</div>
    <div class="tagline">Safe Days Ahead</div>
  </section>

  <div class="side-label side-label--back">BACK</div>
  <section class="card card--back">
    <div class="card__pattern" role="img" aria-label="Faint pattern of pale red flowers with thin stems across the card"></div>
    <svg class="card__corners" viewBox="0 0 754 442" aria-hidden="true">
      <path class="corner--brand" d="M0 0H50C46 72 36 140 0 174Z"/>
      <path class="corner--blush" d="M626 0C626 62 670 102 740 102H754V20H706C692 20 684 12 684 0Z"/>
      <path class="corner--blush" d="M0 334C62 336 116 380 144 442H34C33 418 22 410 0 408Z"/>
      <path class="corner--brand" d="M647 442C647 372 690 330 754 315V442Z"/>
    </svg>
    <div class="brand-ring" aria-hidden="true"></div>
    <div class="person">
      <div class="person__name">MAVIS DUNLEAVY</div>
      <div class="person__role">CLINICAL CARE MANAGER</div>
    </div>
    <ul class="contacts">
      <li class="contacts__item">
        <svg class="contacts__icon" viewBox="0 0 24 24" aria-hidden="true"><path d="M7 2h10a2 2 0 0 1 2 2v16a2 2 0 0 1-2 2H7a2 2 0 0 1-2-2V4a2 2 0 0 1 2-2zm0 2v14h10V4zm4 15h2v1.5h-2z"/></svg>
        <span>0473 856 342</span>
      </li>
      <li class="contacts__item">
        <svg class="contacts__icon" viewBox="0 0 24 24" aria-hidden="true"><path d="M6.6 10.8a15 15 0 0 0 6.6 6.6l2.2-2.2a1 1 0 0 1 1-.25 11.4 11.4 0 0 0 3.6.6 1 1 0 0 1 1 1V20a1 1 0 0 1-1 1A17 17 0 0 1 3 4a1 1 0 0 1 1-1h3.5a1 1 0 0 1 1 1c0 1.250.2 2.450.6 3.6a1 1 0 0 1-.25 1z"/></svg>
        <span>08 7394 2650</span>
      </li>
      <li class="contacts__item">
        <svg class="contacts__icon" viewBox="0 0 24 24" aria-hidden="true"><path d="M2 5h20v14H2zm2 2v.5l8 5 8-5V7z"/></svg>
        <span>mavis@wrenshearthsupport.com.au</span>
      </li>
      <li class="contacts__item">
        <svg class="contacts__icon" viewBox="0 0 24 24" aria-hidden="true"><path d="M12 2a10 10 0 1 0 0 20 10 10 0 0 0 0-20zm-1 2.1V8H7.6A8 8 0 0 1 11 4.1zm2 0A8 8 0 0 1 16.4 8H13zM6.8 10H11v4H6.8a8 8 0 0 1 0-4zm6.2 0h4.2a8 8 0 0 1 0 4H13zM7.6 16H11v3.9A8 8 0 0 1 7.6 16zm5.4 0h3.4a8 8 0 0 1-3.4 3.9z"/></svg>
        <span>www.wrenshearthsupport.com.au</span>
      </li>
      <li class="contacts__item">
        <svg class="contacts__icon" viewBox="0 0 24 24" aria-hidden="true"><path d="M12 2a7 7 0 0 0-7 7c0 5.2 7 13 7 13s7-7.8 7-13a7 7 0 0 0-7-7zm0 9.5A2.5 2.5 0 1 1 12 6.5a2.5 2.5 0 0 1 0 5z"/></svg>
        <span>Gullwing Cove, Western Australia, 6291</span>
      </li>
    </ul>
  </section>

</div>
</body>
</html>
```